Menu Design Project

We trying to replace old flyer/menu with some new design.
hello this is my old menu i attached in email and my logo, the text you can pick from the menu and and i also attached some new picture for the food ,with my menu size unfold. front and back and then fold to 3.5" * 11". please show me what best can you do .Trifold is fine but must have image of food,
this is indian Restaurant
thats fine to have trifold menu design do to short time

Need to add also food picture on menu

Font styles to use
Serif
Decorative
Script

Colors

Designer to choose colors to be used in the design.

Requirements
Must have
• food image on menu
• trifold is fine ( do to short time)
• menu has to elegant ,color or text can be optional, Menu need to be neat and clean no too much rush on between the words .

```html
<!DOCTYPE html>
<html lang="en">
<head>
<meta charset="utf-8">
<title>Saffron Court – Trifold Menu</title>
<link href="https://fonts.googleapis.com/css2?family=Playfair+Display:ital,wght@0,400;0,700;1,400&family=Cormorant+Garamond:wght@500;700&family=Dancing+Script:wght@600&display=swap" rel="stylesheet">
<style>
:root{
  --bg:#e9e9e9;
  --sheet:#1d1d1d;
  --sheet-light:#2a2a2a;
  --gold:#f3d41c;
  --gold-soft:#c8b35a;
  --white:#f4f1e8;
  --line:#3a3a3a;
}
*{box-sizing:border-box;margin:0;padding:0}
html,body{width:1200px;height:1200px;overflow:hidden;background:var(--bg)}
body{font-family:"Playfair Display",Georgia,serif;color:var(--white);font-variant-numeric:lining-nums}
.canvas{width:1200px;height:1200px;padding:20px 30px;display:flex;flex-direction:column;gap:20px}
.sheet{height:570px;display:grid;grid-template-columns:repeat(3,1fr);background:linear-gradient(90deg,var(--sheet) 0%,var(--sheet-light) 33%,var(--sheet) 33.4%,var(--sheet-light) 66.6%,var(--sheet) 67%,var(--sheet-light) 100%);box-shadow:0 4px 14px rgba(0,0,0,.35)}
.panel{padding:14px 16px;display:flex;flex-direction:column;gap:6px;border-right:1px solid var(--line);overflow:hidden}
.panel:last-child{border-right:none}
.tag{align-self:center;display:flex;align-items:center;gap:6px;margin:4px 0 2px}
.tag::before,.tag::after{content:"";width:18px;height:2px;background:var(--gold)}
.tag span{background:var(--gold);color:#151515;font-family:"Dancing Script",cursive;font-size:12.5px;padding:2px 16px;border-radius:3px;border:1px solid #151515;outline:1px solid var(--gold)}
.cols{display:grid;grid-template-columns:1fr 1fr;column-gap:16px}
.col{display:flex;flex-direction:column;gap:3px}
.item{display:grid;grid-template-columns:1fr auto;column-gap:4px;min-height:16px}
.name{font-family:"Cormorant Garamond",serif;font-weight:700;font-size:8px;text-transform:uppercase;letter-spacing:.2px;color:var(--white)}
.price{font-family:"Cormorant Garamond",serif;font-weight:700;font-size:8px;color:var(--white);font-variant-numeric:lining-nums}
.desc{grid-column:1/-1;font-size:5.3px;color:var(--gold-soft);line-height:1.2}
.note{font-size:7px;text-align:center;color:var(--white);margin-top:6px}
.contact{text-align:center;font-size:9px;line-height:1.5;margin-top:auto;padding-bottom:18px}
.contact .rule{width:150px;height:2px;background:var(--gold);margin:0 auto 4px}
.plate{align-self:center;border-radius:50%;border:3px solid #f2f2f2;outline:1px dashed #888;outline-offset:4px}
.brand{text-align:center;display:flex;flex-direction:column;align-items:center;gap:6px;padding-top:16px}
.brand-mark{width:34px;height:34px;border-radius:50%;border:2px solid var(--white)}
.brand-name{font-size:19px;color:var(--white)}
.brand-sub{font-family:"Playfair Display",serif;font-weight:700;font-size:13px;color:var(--white);border-top:2px solid var(--gold);border-bottom:2px solid var(--gold);padding:3px 10px;width:250px}
.frame{margin:14px auto 4px;width:200px;height:170px;border:3px solid var(--gold);padding:5px;outline:1px solid var(--gold);outline-offset:6px}
.frame div{width:100%;height:100%;background:linear-gradient(180deg,#6b5a45 0%,#a98b66 50%,#d9c7a8 100%)}
.hours{text-align:center;margin-top:16px;display:flex;flex-direction:column;gap:2px}
.hours h3{font-family:"Playfair Display",serif;color:var(--gold);font-size:12px;font-weight:700;margin-top:6px}
.hours p{font-size:9px;color:var(--white)}
.halal{display:flex;align-items:center;justify-content:center;gap:6px;margin-top:12px;font-size:11px;font-weight:700}
.halal::before,.halal::after{content:"";width:40px;height:2px;background:var(--gold)}
.web{text-align:center;font-style:italic;font-size:9px;color:var(--gold);letter-spacing:1px}
</style>
</head>
<body>
<main class="canvas">

<section class="sheet">
  <div class="panel">
    <div class="tag"><span>Handi (Vegetarian)</span></div>
    <div class="cols">
      <div class="col">
        <div class="item"><span class="name">Paneer Makhni</span><span class="price">$8.99</span><span class="desc">paneer in creamy tomato sauce</span></div>
        <div class="item"><span class="name">Paneer Tikka Masala</span><span class="price">$8.99</span><span class="desc">grilled paneer in spiced gravy</span></div>
        <div class="item"><span class="name">Kadai Paneer</span><span class="price">$8.99</span><span class="desc">paneer with peppers and onion</span></div>
        <div class="item"><span class="name">Palak Paneer</span><span class="price">$8.44</span><span class="desc">spinach with cottage cheese</span></div>
        <div class="item"><span class="name">Mutter Paneer</span><span class="price">$8.49</span><span class="desc">green peas with paneer</span></div>
        <div class="item"><span class="name">Shahi Paneer</span><span class="price">$8.99</span><span class="desc">paneer in rich cashew cream</span></div>
        <div class="item"><span class="name">Paneer Bhurji</span><span class="price">$10.99</span><span class="desc">scrambled paneer with spices</span></div>
        <div class="item"><span class="name">Malai Kofta</span><span class="price">$8.99</span><span class="desc">vegetable balls in creamy sauce</span></div>
        <div class="item"><span class="name">Navratan Korma</span><span class="price">$8.99</span><span class="desc">nine vegetables in mild cream</span></div>
        <div class="item"><span class="name">Kaju Mushroom Mutter</span><span class="price">$9.29</span><span class="desc">mushroom, cashew and green peas</span></div>
        <div class="item"><span class="name">Methi Malai Mutter</span><span class="price">$9.29</span><span class="desc">peas with fenugreek cream</span></div>
        <div class="item"><span class="name">Aloo Gobhi</span><span class="price">$8.50</span><span class="desc">potato and cauliflower dry curry</span></div>
      </div>
      <div class="col">
        <div class="item"><span class="name">Bhindi Masala</span><span class="price">$8.50</span><span class="desc">okra with onion and tomato</span></div>
        <div class="item"><span class="name">Achari Baigan</span><span class="price">$8.49</span><span class="desc">baby eggplant in pickle spices</span></div>
        <div class="item"><span class="name">Baigan Bhartha</span><span class="price">$8.49</span><span class="desc">smoked mashed eggplant</span></div>
        <div class="item"><span class="name">Vegetable Jalfrezi</span><span class="price">$8.49</span><span class="desc">mixed vegetables in tangy sauce</span></div>
        <div class="item"><span class="name">Zeera Aloo</span><span class="price">$7.50</span><span class="desc">potatoes tossed with cumin</span></div>
        <div class="item"><span class="name">Sarson Ka Saag</span><span class="price">$8.49</span><span class="desc">mustard greens, Punjabi style</span></div>
        <div class="item"><span class="name">Chana Peshawari</span><span class="price">$8.49</span><span class="desc">chickpeas in Peshawari spices</span></div>
        <div class="item"><span class="name">Chana Palak</span><span class="price">$8.49</span><span class="desc">chickpeas with fresh spinach</span></div>
        <div class="item"><span class="name">Punjabi Kadi</span><span class="price">$8.49</span><span class="desc">yogurt curry with dumplings</span></div>
        <div class="item"><span class="name">Daal Tarka Yellow</span><span class="price">$8.49</span><span class="desc">yellow lentils with garlic</span></div>
        <div class="item"><span class="name">Daal Tarka Black</span><span class="price">$8.49</span><span class="desc">black lentils with ginger</span></div>
        <div class="item"><span class="name">Daal Makhni</span><span class="price">$8.49</span><span class="desc">black lentils in butter</span></div>
      </div>
    </div>
    <div class="tag"><span>Tandoori Bread</span></div>
    <div class="cols">
      <div class="col">
        <div class="item"><span class="name">Tandoori Roti</span><span class="price">$1.75</span><span class="desc">whole wheat clay oven bread</span></div>
        <div class="item"><span class="name">Tandoori Naan</span><span class="price">$1.75</span><span class="desc">white flour clay oven bread</span></div>
        <div class="item"><span class="name">Garlic Naan</span><span class="price">$2.50</span><span class="desc">naan topped with garlic</span></div>
        <div class="item"><span class="name">Lachha Paratha</span><span class="price">$2.50</span><span class="desc">layered whole wheat bread</span></div>
        <div class="item"><span class="name">Onion Kulcha</span><span class="price">$2.99</span><span class="desc">bread stuffed with onion</span></div>
      </div>
      <div class="col">
        <div class="item"><span class="name">Aloo Paratha</span><span class="price">$2.99</span><span class="desc">stuffed with spiced potato</span></div>
        <div class="item"><span class="name">Gobhi Paratha</span><span class="price">$3.50</span><span class="desc">stuffed with spiced cauliflower</span></div>
        <div class="item"><span class="name">Pudina Paratha</span><span class="price">$2.99</span><span class="desc">flavored with fresh mint</span></div>
        <div class="item"><span class="name">Keema Naan</span><span class="price">$3.99</span><span class="desc">stuffed with minced chicken</span></div>
        <div class="item"><span class="name">Jalebi Paratha</span><span class="price">$2.99</span><span class="desc">crisp sweet layered bread</span></div>
      </div>
    </div>
    <div class="tag"><span>Desserts</span></div>
    <div class="cols">
      <div class="col"><div class="item"><span class="name">Kheer</span><span class="price">$3.99</span><span class="desc">rice pudding with nuts</span></div></div>
      <div class="col"><div class="item"><span class="name">Rasmalai (3 pcs)</span><span class="price">$3.99</span><span class="desc">cheese dumplings in milk</span></div></div>
    </div>
  </div>

  <div class="panel">
    <div class="cols">
      <div class="col">
        <div class="item"><span class="name">Gulab Jamun (3 pc.)</span><span class="price">$3.99</span><span class="desc">milk dumplings in syrup</span></div>
        <div class="item"><span class="name">Gajar Halwa</span><span class="price">$3.99</span><span class="desc">carrot pudding with nuts</span></div>
      </div>
      <div class="col">
        <div class="item"><span class="name">Ice Cream</span><span class="price">$3.50</span><span class="desc">mango or vanilla</span></div>
      </div>
    </div>
    <div class="tag"><span>Beverages</span></div>
    <div class="cols">
      <div class="col">
        <div class="item"><span class="name">Mango Lassi</span><span class="price">$3.50</span><span class="desc">mango yogurt drink</span></div>
        <div class="item"><span class="name">Lassi (sweet or salted)</span><span class="price">$3.50</span><span class="desc">chilled yogurt drink</span></div>
        <div class="item"><span class="name">Fresh Lemonade</span><span class="price">$2.99</span><span class="desc">sweet and sour lemon</span></div>
        <div class="item"><span class="name">Pina Colada Virgin</span><span class="price">$3.99</span><span class="desc">pineapple and coconut</span></div>
        <div class="item"><span class="name">Strawberry Daiquiri Virgin</span><span class="price">$3.99</span><span class="desc">strawberry and lime blend</span></div>
        <div class="item"><span class="name">Orange Juice</span><span class="price">$2.99</span></div>
        <div class="item"><span class="name">Pineapple Juice</span><span class="price">$2.99</span></div>
      </div>
      <div class="col">
        <div class="item"><span class="name">Mango Juice</span><span class="price">$2.99</span></div>
        <div class="item"><span class="name">Masala Tea</span><span class="price">$1.99</span><span class="desc">spiced Indian milk tea</span></div>
        <div class="item"><span class="name">Coffee</span><span class="price">$1.99</span></div>
        <div class="item"><span class="name">Cold Beers</span><span class="price"></span><span class="desc">ask for our selection</span></div>
        <div class="item"><span class="name">Indian Beers</span><span class="price"></span></div>
        <div class="item"><span class="name">Wines (750ml / 1.5 Ltr)</span><span class="price">$22.00/$38.00</span><span class="desc">red, white and rose</span></div>
        <div class="item"><span class="name">Cola, Lemon Soda, Ginger Ale</span><span class="price">$1.50</span></div>
      </div>
    </div>
    <div class="tag"><span>Cocktails</span></div>
    <div class="cols">
      <div class="col">
        <div class="item"><span class="name">Martini Coctail</span><span class="price">$6.99</span><span class="desc">house mixed classic</span></div>
        <div class="item"><span class="name">Mojito Coctail</span><span class="price">$8.99</span><span class="desc">house mixed classic</span></div>
        <div class="item"><span class="name">White Rum Coctail</span><span class="price">$5.99</span><span class="desc">house mixed classic</span></div>
        <div class="item"><span class="name">Mai Tai Coctail</span><span class="price">$4.99</span><span class="desc">house mixed classic</span></div>
        <div class="item"><span class="name">Bloody Mary</span><span class="price">$9.99</span><span class="desc">house mixed classic</span></div>
        <div class="item"><span class="name">Daiquiri Coctail</span><span class="price">$10.99</span><span class="desc">house mixed classic</span></div>
        <div class="item"><span class="name">Tropical Storm</span><span class="price">$6.99</span><span class="desc">house mixed classic</span></div>
        <div class="item"><span class="name">Pina Colada</span><span class="price">$6.99</span><span class="desc">house mixed classic</span></div>
        <div class="item"><span class="name">Tequila Blond</span><span class="price">$6.99</span><span class="desc">house mixed classic</span></div>
      </div>
      <div class="col">
        <div class="item"><span class="name">Banana D Coctail</span><span class="price">$6.99</span><span class="desc">house mixed classic</span></div>
        <div class="item"><span class="name">Cuban Rum</span><span class="price">$8.99</span><span class="desc">house mixed classic</span></div>
        <div class="item"><span class="name">Mango Daiquiri</span><span class="price">$5.99</span><span class="desc">house mixed classic</span></div>
        <div class="item"><span class="name">Cuban Mojito</span><span class="price">$4.99</span><span class="desc">house mixed classic</span></div>
        <div class="item"><span class="name">Bloody Mary</span><span class="price">$9.99</span><span class="desc">house mixed classic</span></div>
        <div class="item"><span class="name">Daiquiri Coctail</span><span class="price">$10.99</span><span class="desc">house mixed classic</span></div>
        <div class="item"><span class="name">Mai Tai Cocktail</span><span class="price">$6.99</span><span class="desc">house mixed classic</span></div>
        <div class="item"><span class="name">Bloody Ma Cocktail</span><span class="price">$8.99</span><span class="desc">house mixed classic</span></div>
        <div class="item"><span class="name">Daiquiri Cocktail</span><span class="price">$6.99</span><span class="desc">house mixed classic</span></div>
      </div>
    </div>
    <p class="note">[Prices subject to change without notice. Tax is not included in these prices]</p>
    <div class="contact">
      <div class="rule"></div>
      <p>240 Orchard Lane, Maple Heights, NY 10990</p>
      <p>Email: HELLO@SAFFRONCOURTNY.COM</p>
      <p>Tel: 555-014-2200, 555-014-2210</p>
      <p>Fax: 555-014-2299</p>
    </div>
  </div>

  <div class="panel">
    <div class="brand">
      <div class="brand-mark"></div>
      <div class="brand-name">Saffron Court</div>
      <div class="brand-sub">RESTAURANT &amp; BANQUET HALL</div>
    </div>
    <div class="frame"><div role="img" aria-label="Photo of the restaurant dining room interior"></div></div>
    <div class="hours">
      <h3>Lunch Hours:</h3><p>Mon - Sun <b>11:30am - 3:30pm</b></p>
      <h3>Dinner Hours:</h3><p>Mon - Sun <b>3:30pm - 11:00pm</b></p>
      <h3>Lunch Special:</h3><p>Mon - Sun: <b>11:30 AM - 04:00 PM</b></p>
    </div>
    <div class="halal">WE SERVED HALAL FOOD</div>
    <div class="web">www.saffroncourtny.com</div>
  </div>
</section>

<section class="sheet">
  <div class="panel">
    <div class="tag"><span>Vegetarian Appetizer</span></div>
    <div class="cols">
      <div class="col">
        <div class="item"><span class="name">Vegetable Samosa (2 pc.)</span><span class="price">$2.99</span><span class="desc">spiced potato pastry</span></div>
        <div class="item"><span class="name">Samosa Chaat (2 pc.)</span><span class="price">$7.49</span><span class="desc">samosa with chickpeas, chutney</span></div>
        <div class="item"><span class="name">Aloo Tikki Chaat (4 pc.)</span><span class="price">$6.99</span><span class="desc">potato patties with chutney</span></div>
        <div class="item"><span class="name">Mix Veg. Pakora</span><span class="price">$6.50</span><span class="desc">fried vegetable fritters</span></div>
        <div class="item"><span class="name">Papri Chaat</span><span class="price">$6.50</span><span class="desc">crisps with yogurt, tamarind</span></div>
        <div class="item"><span class="name">Dahi Bhalla</span><span class="price">$6.99</span><span class="desc">lentil balls in yogurt</span></div>
      </div>
      <div class="col">
        <div class="item"><span class="name">Paneer Pakora (7 pc.)</span><span class="price">$8.95</span><span class="desc">fried cheese fritters</span></div>
        <div class="item"><span class="name">Vegetable Seekh Kabab</span><span class="price">$8.99</span><span class="desc">minced vegetable skewers</span></div>
        <div class="item"><span class="name">Paneer Tikka Tandoori</span><span class="price">$11.99</span><span class="desc">grilled paneer with peppers</span></div>
        <div class="item"><span class="name">Chhole Bhature (2 pc.)</span><span class="price">$8.99</span><span class="desc">chickpeas with fried bread</span></div>
        <div class="item"><span class="name">Stuffed Paneer Pakora (6 pc.)</span><span class="price">$8.50</span><span class="desc">paneer stuffed with mint</span></div>
        <div class="item"><span class="name">Chatpati Aloo Chaat</span><span class="price">$7.50</span></div>
      </div>
    </div>
    <div class="tag"><span>Non Vegetarian Appetizer</span></div>
    <div class="cols">
      <div class="col">
        <div class="item"><span class="name">Chicken Samosa (2 pc.)</span><span class="price">$5.99</span><span class="desc">minced chicken pastry</span></div>
        <div class="item"><span class="name">Chicken Pakora</span><span class="price">$10.99</span><span class="desc">battered fried chicken</span></div>
        <div class="item"><span class="name">Fish Amritsari</span><span class="price">$14.59</span><span class="desc">spiced fried fish</span></div>
        <div class="item"><span class="name">Tawa Chicken</span><span class="price">$12.99</span><span class="desc">chicken on hot griddle</span></div>
        <div class="item"><span class="name">Garlic Shrimp</span><span class="price">$12.99</span><span class="desc">shrimp in garlic sauce</span></div>
        <div class="item"><span class="name">Spicy Wings (8 pc.)</span><span class="price">$8.99</span><span class="desc">tossed in hot sauce</span></div>
        <div class="item"><span class="name">Tandoori Chicken</span><span class="price">$8.99/12.29</span><span class="desc">marinated, clay oven roasted</span></div>
        <div class="item"><span class="name">Chicken Seekh Kabab</span><span class="price">$10.49</span><span class="desc">minced chicken skewers</span></div>
        <div class="item"><span class="name">Lamb Seekh Kabab</span><span class="price">$12.29</span><span class="desc">minced lamb skewers</span></div>
        <div class="item"><span class="name">Chicken Tikka</span><span class="price">$11.49</span><span class="desc">boneless chicken in clay oven</span></div>
      </div>
      <div class="col">
        <div class="item"><span class="name">Chicken Malai Kabab</span><span class="price">$11.99</span><span class="desc">creamy mild chicken kabab</span></div>
        <div class="item"><span class="name">Achari Tikka</span><span class="price">$11.99</span><span class="desc">chicken in pickle spices</span></div>
        <div class="item"><span class="name">Afghani Chicken</span><span class="price">$12.99</span><span class="desc">chicken in cashew cream</span></div>
        <div class="item"><span class="name">Fish Tikka Tandoori</span><span class="price">$14.99</span><span class="desc">fish cubes from clay oven</span></div>
        <div class="item"><span class="name">Salmon Fish</span><span class="price">$15.29</span><span class="desc">salmon with herbs</span></div>
        <div class="item"><span class="name">Tawa Fish</span><span class="price">$14.99</span><span class="desc">fish on hot griddle</span></div>
        <div class="item"><span class="name">Tandoori Shrimp (6 pc.)</span><span class="price">$14.99</span><span class="desc">jumbo shrimp, clay oven</span></div>
        <div class="item"><span class="name">Lamb Chop (5 pc.)</span><span class="price">$22.99</span><span class="desc">marinated lamb chops</span></div>
        <div class="item"><span class="name">Tandoori Mix Grill</span><span class="price">$18.49</span><span class="desc">chicken, kabab and shrimp</span></div>
      </div>
    </div>
    <div class="plate" style="width:150px;height:60px;margin-top:auto;margin-bottom:8px;background:radial-gradient(ellipse at center,#c2461c 0%,#8e2e12 55%,#f2f2f2 58%)" role="img" aria-label="Photo of a plate of fried chicken appetizer"></div>
  </div>

  <div class="panel">
    <div class="tag"><span>Indo-Chinese</span></div>
    <div class="cols">
      <div class="col">
        <div class="item"><span class="name">Chilli Paneer</span><span class="price">$10.99</span><span class="desc">paneer with peppers, onion</span></div>
        <div class="item"><span class="name">Chilli Mushroom</span><span class="price">$9.99</span><span class="desc">mushroom with peppers, onion</span></div>
        <div class="item"><span class="name">Chilli Gobhi</span><span class="price">$9.99</span><span class="desc">crisp cauliflower in chilli</span></div>
        <div class="item"><span class="name">Vegetable Manchurian</span><span class="price">$10.50</span><span class="desc">vegetable balls in sauce</span></div>
        <div class="item"><span class="name">Vegetable Chowmin</span><span class="price">$8.30</span><span class="desc">noodles with vegetables</span></div>
        <div class="item"><span class="name">Vegetable Spring Roll</span><span class="price">$6.99</span><span class="desc">crisp vegetable rolls</span></div>
        <div class="item"><span class="name">Chilli Chicken</span><span class="price">$10.99</span><span class="desc">chicken with peppers, onion</span></div>
      </div>
      <div class="col">
        <div class="item"><span class="name">Chilli Fish</span><span class="price">$13.99</span><span class="desc">fish with peppers, onion</span></div>
        <div class="item"><span class="name">Chilli Shrimp</span><span class="price">$12.99</span><span class="desc">shrimp with peppers, onion</span></div>
        <div class="item"><span class="name">Chicken Manchurian</span><span class="price">$10.99</span><span class="desc">chicken in Manchurian sauce</span></div>
        <div class="item"><span class="name">Chicken Chowmin</span><span class="price">$9.99</span><span class="desc">noodles with chicken</span></div>
        <div class="plate" style="width:62px;height:62px;margin-top:4px;background:radial-gradient(circle,#e2c070 0%,#c79a3e 45%,#f2f2f2 50%)" role="img" aria-label="Photo of a bowl of noodles"></div>
      </div>
    </div>
    <div class="tag"><span>Soup, Salad &amp; Raita</span></div>
    <div class="cols">
      <div class="col">
        <div class="item"><span class="name">Tomato Soup</span><span class="price">$3.99</span><span class="desc">fresh tomato soup</span></div>
        <div class="item"><span class="name">Vegetable Soup</span><span class="price">$3.99</span><span class="desc">mixed vegetable soup</span></div>
        <div class="item"><span class="name">Chicken Soup</span><span class="price">$4.50</span><span class="desc">classic chicken broth</span></div>
        <div class="item"><span class="name">Hot N Sour Soup (chicken or veg)</span><span class="price">$4.99</span><span class="desc">spicy and tangy</span></div>
      </div>
      <div class="col">
        <div class="item"><span class="name">Fresh Garden Salad</span><span class="price">$4.50</span></div>
        <div class="item"><span class="name">Masala Salad</span><span class="price">$5.99</span></div>
        <div class="item"><span class="name">Mix Raita</span><span class="price">$3.99</span></div>
        <div class="item"><span class="name">Boondi Raita</span><span class="price">$3.99</span></div>
        <div class="item"><span class="name">Pudina Raita</span><span class="price">$3.99</span></div>
        <div class="item"><span class="name">Plain Dahi</span><span class="price">$3.50</span></div>
      </div>
    </div>
    <div class="tag"><span>Seafood Special</span></div>
    <div class="cols">
      <div class="col">
        <div class="item"><span class="name">Kadai Fish</span><span class="price">$13.99</span><span class="desc">fish with peppers, onion</span></div>
        <div class="item"><span class="name">Fish Curry</span><span class="price">$13.99</span><span class="desc">fish in onion gravy</span></div>
        <div class="item"><span class="name">Fish Masala</span><span class="price">$13.99</span><span class="desc">fish in spiced sauce</span></div>
        <div class="item"><span class="name">Goa Fish Curry</span><span class="price">$12.59</span><span class="desc">coconut fish curry</span></div>
        <div class="item"><span class="name">Fish Tikka Masala</span><span class="price">$12.59</span><span class="desc">fish in creamy sauce</span></div>
        <div class="item"><span class="name">Shrimp Curry</span><span class="price">$12.99</span><span class="desc">shrimp in onion gravy</span></div>
        <div class="item"><span class="name">Shrimp Bhuna</span><span class="price">$12.99</span><span class="desc">shrimp with onion, tomato</span></div>
      </div>
      <div class="col">
        <div class="item"><span class="name">Shrimp Vindaloo</span><span class="price">$12.99</span><span class="desc">shrimp with potato, vinegar</span></div>
        <div class="item"><span class="name">Kadai Shrimp</span><span class="price">$12.99</span><span class="desc">shrimp with ginger, pepper</span></div>
        <div class="item"><span class="name">Shrimp Masala</span><span class="price">$12.99</span><span class="desc">shrimp in spiced sauce</span></div>
        <div class="item"><span class="name">Shrimp Saag</span><span class="price">$12.99</span><span class="desc">shrimp with spinach</span></div>
        <div class="plate" style="width:80px;height:50px;border-radius:6px;margin-top:4px;background:linear-gradient(135deg,#d9542a,#a8321a)" role="img" aria-label="Photo of a seafood dish on a square plate"></div>
      </div>
    </div>
  </div>

  <div class="panel">
    <div class="tag"><span>Handi Special (Non Veg)</span></div>
    <div class="cols">
      <div class="col">
        <div class="item"><span class="name">Chicken Makhni</span><span class="price">$9.49</span><span class="desc">chicken in butter sauce</span></div>
        <div class="item"><span class="name">Chicken Tikka Masala</span><span class="price">$9.49</span><span class="desc">grilled chicken in cream</span></div>
        <div class="item"><span class="name">Chicken Curry</span><span class="price">$9.29</span><span class="desc">chicken in onion gravy</span></div>
        <div class="item"><span class="name">Chicken Korma</span><span class="price">$9.29</span><span class="desc">chicken in cashew cream</span></div>
        <div class="item"><span class="name">Kadai Chicken</span><span class="price">$9.29</span><span class="desc">chicken with peppers, onion</span></div>
        <div class="item"><span class="name">Chicken Saag</span><span class="price">$8.99</span><span class="desc">chicken with spinach</span></div>
        <div class="item"><span class="name">Chicken Jalfrezi</span><span class="price">$8.99</span><span class="desc">chicken with fresh vegetables</span></div>
        <div class="item"><span class="name">Chicken Masala</span><span class="price">$9.99</span><span class="desc">chicken in spiced sauce</span></div>
        <div class="item"><span class="name">Chicken Vindaloo</span><span class="price">$9.99</span><span class="desc">chicken with potato, vinegar</span></div>
        <div class="item"><span class="name">Goat Curry</span><span class="price">$10.29</span><span class="desc">goat in onion gravy</span></div>
        <div class="item"><span class="name">Goat Masala</span><span class="price">$11.29</span><span class="desc">goat in spiced sauce</span></div>
        <div class="item"><span class="name">Kadai Goat</span><span class="price">$10.29</span><span class="desc">goat with peppers, onion</span></div>
      </div>
      <div class="col">
        <div class="item"><span class="name">Goat Saag</span><span class="price">$9.99</span><span class="desc">goat with spinach</span></div>
        <div class="item"><span class="name">Goat Vindaloo</span><span class="price">$9.99</span><span class="desc">goat with potato, vinegar</span></div>
        <div class="item"><span class="name">Chicken Keema Mutter</span><span class="price">$10.99</span><span class="desc">minced chicken with peas</span></div>
        <div class="item"><span class="name">Lamb Curry</span><span class="price">$10.99</span><span class="desc">lamb in onion gravy</span></div>
        <div class="item"><span class="name">Lamb Rogan Josh</span><span class="price">$10.99</span><span class="desc">Kashmiri style lamb</span></div>
        <div class="item"><span class="name">Lamb Saag</span><span class="price">$10.99</span><span class="desc">lamb with spinach</span></div>
        <div class="item"><span class="name">Lamb Korma</span><span class="price">$10.99</span><span class="desc">lamb in cashew cream</span></div>
        <div class="item"><span class="name">Lamb Bhuna Ghost</span><span class="price">$10.99</span><span class="desc">lamb with onion, tomato</span></div>
        <div class="item"><span class="name">Lamb Vindaloo</span><span class="price">$10.99</span><span class="desc">lamb with potato, vinegar</span></div>
        <div class="item"><span class="name">Lamb Keema Mutter</span><span class="price">$12.99</span><span class="desc">minced lamb with peas</span></div>
        <div class="plate" style="width:58px;height:58px;margin-top:4px;background:radial-gradient(circle,#e9d9b0 0%,#b88a4a 45%,#f2f2f2 50%)" role="img" aria-label="Photo of a curry bowl"></div>
      </div>
    </div>
    <div class="tag"><span>Biryani &amp; Rice</span></div>
    <div class="cols">
      <div class="col">
        <div class="item"><span class="name">Chicken Biryani</span><span class="price">$7.99</span><span class="desc">chicken with basmati rice</span></div>
        <div class="item"><span class="name">Goat Biryani</span><span class="price">$9.99</span><span class="desc">goat with basmati rice</span></div>
        <div class="item"><span class="name">Lamb Biryani</span><span class="price">$9.99</span><span class="desc">lamb with basmati rice</span></div>
        <div class="item"><span class="name">Shrimp Biryani</span><span class="price">$10.99</span><span class="desc">shrimp with basmati rice</span></div>
      </div>
      <div class="col">
        <div class="item"><span class="name">Vegetable Biryani</span><span class="price">$7.99</span><span class="desc">vegetables with basmati rice</span></div>
        <div class="item"><span class="name">Zeera Rice</span><span class="price">$3.99</span><span class="desc">rice with cumin</span></div>
        <div class="item"><span class="name">Peas Pulao</span><span class="price">$5.99</span><span class="desc">rice with green peas</span></div>
        <div class="item"><span class="name">House Spl. Biryani</span><span class="price">$11.99</span><span class="desc">chicken, lamb and shrimp</span></div>
      </div>
    </div>
    <div class="plate" style="width:120px;height:52px;margin-top:auto;margin-bottom:8px;background:radial-gradient(ellipse at center,#d8a24a 0%,#b87a2e 55%,#f2f2f2 58%)" role="img" aria-label="Photo of a plate of biryani"></div>
  </div>
</section>

</main>
</body>
</html>
```